Visitenkarten-Design für Stillberaterin
Zielgruppe
Ich bin Stillberaterin ZMRPT, d. h. ich berate Mütter bei Stillschwierigkeiten. Meine Zielgruppe sind junge Familien, die sich vorab über das Stillen Ihres Kindes informieren möchten, Stillschwierigkeiten (z. B. Schmerzen, schlechte Gewichtszunahme usw.) haben oder Fragen rund ums Stillen haben (Medikamente, Stillen in besonderen Situationen...). Weiterhin biete ich Kurse für den Beikoststart oder zum Abstillen an.
Aufgabenstellung
Auf meiner Visitenkarte sollte mein Logo sowie alle Kontaktdaten klar und deutlich erkennbar sein. Die Farben sind dem Logo anzupassen. Die Schriftarten, die im Logo verwendet werden sind: Be Bright und Apple Tree

```html
<!DOCTYPE html>
<html lang="de">
<head>
<meta charset="utf-8">
<title>Visitenkarte Stillberatung</title>
<link rel="stylesheet" href="https://fonts.googleapis.com/css2?family=Dancing+Script:wght@400;600&family=Open+Sans:wght@400&family=Varela+Round&display=swap">
<style>
  :root {
    --backdrop: #c8c8c8;
    --paper: #ffffff;
    --rose: #ec5fa6;
    --rose-soft: #f6b3d4;
    --rose-faint: #fbe0ee;
    --ink: #2b2b2b;
    --grey-script: #6f6f6f;
  }
  * { margin: 0; padding: 0; box-sizing: border-box; }
  html, body { width: 1073px; height: 1200px; overflow: hidden; background: var(--backdrop); }
  .sheet { position: relative; width: 1073px; height: 1200px; }
  .card {
    position: absolute; left: 157px; width: 796px; height: 505px;
    background: var(--paper);
    box-shadow: 1px 2px 4px rgba(0,0,0,0.25);
  }
  .card--front { top: 73px; }
  .card--back { top: 647px; }
  .frame {
    position: absolute; left: 31px; top: 37px; right: 35px; bottom: 31px;
    border: 1.5px solid var(--rose); border-radius: 6px;
  }
  .corner {
    position: absolute; width: 66px; height: 66px;
    background: var(--rose-faint);
  }
  .corner--tl { left: 29px; top: 35px; }
  .corner--tr { right: 33px; top: 35px; }
  .corner--bl { left: 29px; bottom: 29px; }
  .corner--br { right: 33px; bottom: 29px; }

  .brand-slot {
    position: absolute; left: 98px; top: 234px; width: 200px;
    display: flex; align-items: center; justify-content: center; gap: 8px;
    font-family: "Open Sans", sans-serif; font-weight: 400; font-size: 23px; color: var(--rose);
  }
  .brand-dot { width: 11px; height: 11px; border-radius: 50%; background: var(--rose); flex: none; }

  .holder-name {
    position: absolute; left: 337px; top: 100px;
    font-family: "Dancing Script", cursive; font-weight: 400; font-size: 54px; color: var(--grey-script);
    line-height: 1; white-space: nowrap;
  }
  .holder-role {
    position: absolute; left: 342px; top: 181px;
    font-family: "Varela Round", sans-serif; font-size: 18px; line-height: 27.5px; color: var(--ink);
  }
  .address {
    position: absolute; left: 342px; top: 268px;
    font-family: "Open Sans", sans-serif; font-size: 23px; line-height: 33px; color: var(--ink);
  }
  .contact {
    position: absolute; left: 343px; top: 353px; list-style: none;
    font-family: "Open Sans", sans-serif; font-size: 23px; line-height: 34px; color: var(--ink);
  }
  .contact li { display: flex; align-items: center; gap: 13px; white-space: nowrap; }
  .contact svg { width: 21px; height: 21px; fill: var(--rose); flex: none; }

  .back-brand {
    position: absolute; left: 0; right: 0; top: 255px; text-align: center;
    font-family: "Open Sans", sans-serif; font-weight: 400; font-size: 44px; color: var(--rose); line-height: 1;
  }
  .back-tagline {
    position: absolute; left: 0; right: 0; top: 310px; text-align: center;
    font-family: "Varela Round", sans-serif; font-size: 14px; color: var(--rose-soft);
  }
  .web {
    position: absolute; left: 0; right: 0; top: 412px; text-align: center;
    font-family: "Dancing Script", cursive; font-weight: 400; font-size: 34px; color: var(--rose);
    line-height: 44px;
  }
  .flourish {
    position: absolute; top: 434px; width: 94px; height: 8px; border-radius: 4px;
    background: linear-gradient(90deg, var(--rose-faint), var(--rose-soft), var(--rose-faint));
  }
  .flourish--left { left: 147px; }
  .flourish--right { left: 559px; }
</style>
</head>
<body>
<main class="sheet">
  <section class="card card--front">
    <div class="frame"></div>
    <div class="corner corner--tl" role="img" aria-label="Rankenornament Ecke"></div>
    <div class="corner corner--tr" role="img" aria-label="Rankenornament Ecke"></div>
    <div class="corner corner--bl" role="img" aria-label="Rankenornament Ecke"></div>
    <div class="corner corner--br" role="img" aria-label="Rankenornament Ecke"></div>

    <div class="brand-slot"><span class="brand-dot"></span>Stillzeit-Nest</div>

    <h1 class="holder-name">Rubinka Tovik</h1>
    <p class="holder-role">Fachkinderkrankenschwester,<br>Still- &amp; Laktationsberaterin ZMRPT</p>
    <p class="address">Am Lindenhang 4<br>98765 Feldmoosing</p>
    <ul class="contact">
      <li>
        <svg viewBox="0 0 24 24" aria-hidden="true"><path d="M6.6 10.8a15.1 15.1 0 0 0 6.6 6.6l2.2-2.2c.3-.3.7-.4 1-.2 1.1.4 2.3.6 3.6.6.6 0 1 .4 1 1V20c0 .6-.4 1-1 1A17 17 0 0 1 3 4c0-.6.4-1 1-1h3.5c.6 0 1 .4 1 1 0 1.3.2 2.5.6 3.6.1.3 0 .7-.2 1z"/></svg>
        01234 5550187
      </li>
      <li>
        <svg viewBox="0 0 24 24" aria-hidden="true"><path d="M2 5h20v14H2z"/><path d="M2.5 5.5l9.5 7.5 9.5-7.5M2.5 18.5l7-6M21.5 18.5l-7-6" stroke="#fff" stroke-width="1.3" fill="none"/></svg>
        rubinka7@stillzeit-nest.de
      </li>
    </ul>
  </section>

  <section class="card card--back">
    <div class="frame"></div>
    <div class="corner corner--tl" role="img" aria-label="Rankenornament Ecke"></div>
    <div class="corner corner--tr" role="img" aria-label="Rankenornament Ecke"></div>
    <div class="corner corner--bl" role="img" aria-label="Rankenornament Ecke"></div>
    <div class="corner corner--br" role="img" aria-label="Rankenornament Ecke"></div>

    <h2 class="back-brand">Stillzeit-Nest</h2>
    <p class="back-tagline">Stillberatung für Feldmoosing</p>

    <div class="flourish flourish--left" role="img" aria-label="Schnörkelornament"></div>
    <p class="web">www.stillzeit-nest.de</p>
    <div class="flourish flourish--right" role="img" aria-label="Schnörkelornament"></div>
  </section>
</main>
</body>
</html>
```